Home Improvement Company in need of a "Banner & Billboard Design"

I'm Looking for a Banner design 4X6 With Company Logo, Phone Number, website, Credentials and services.. I picture a charcoal/matte background i also want to look like a house shape design i will upload the sample...

I'm looking for a Billboard design to target homeowners who need Roofing Services. I need logo, number, website, KTL, Credentials and a catchy title. i will like to use the same colors for branding

Target Market(s)

Homeowners, Investors,

Industry/Entity Type

Home Improvement

Font styles to use
Decorative

Colors
00a990
5c5c5c
333333

Requirements
Must have
• All Credentials, Phone number, website, logo, logo colors, services, Eye Catchy, Direct Message, Friendly feeling,
• (614) 372 - 9058
• Roofing Gutters Painting Pressure Washing Exterior Design
Nice to have
• A catchy title, A direct message to a homeowner looking for home improvement services. noticeable
Should not have
• not Busy, no

```html
<!DOCTYPE html>
<html lang="en">
<head>
<meta charset="utf-8">
<title>Ridgeview Home Exteriors – Banner &amp; Billboard Set</title>
<link rel="stylesheet" href="https://fonts.googleapis.com/css2?family=Source+Sans+3:wght@400;600;700&display=swap">
<style>
  :root{
    --teal:#00a990;
    --teal-deep:#17917f;
    --gray:#5c5c5c;
    --charcoal:#333333;
    --ink:#1b1b1b;
    --white:#ffffff;
    --badge-blue:#1d4f91;
    --badge-red:#d6262b;
    --badge-gray:#8a8a8a;
  }
  html,body{margin:0;padding:0;width:1006px;height:1200px;overflow:hidden;background:var(--white);}
  .sheet{display:block;width:1006px;height:1200px;font-family:"Source Sans 3",sans-serif;}
  .brand-name{font-family:"Source Sans 3",sans-serif;font-weight:700;fill:var(--teal);letter-spacing:1px;}
  .web{font-weight:400;fill:var(--charcoal);}
  .web--light{fill:var(--white);}
  .phone{font-weight:700;fill:var(--teal);}
  .slogan{font-weight:700;fill:var(--white);}
  .services{font-weight:600;fill:var(--white);letter-spacing:.3px;}
</style>
</head>
<body>
<svg class="sheet" viewBox="0 0 1260 1503" xmlns="http://www.w3.org/2000/svg">
  <defs>
    <linearGradient id="dark-fade" x1="0" y1="0" x2="1" y2="1">
      <stop offset="0" stop-color="#2e2e2e"/><stop offset="1" stop-color="#4a4a4a"/>
    </linearGradient>
    <linearGradient id="night-fade" x1="0" y1="0" x2="1" y2="1">
      <stop offset="0" stop-color="#141414"/><stop offset="1" stop-color="#3a3a3a"/>
    </linearGradient>
    <linearGradient id="slate-fade" x1="0" y1="0" x2="1" y2="1">
      <stop offset="0" stop-color="#3a3a3a"/><stop offset="1" stop-color="#5e5e5e"/>
    </linearGradient>
    <linearGradient id="teal-fade" x1="0" y1="0" x2="1" y2="0">
      <stop offset="0" stop-color="#0fa089"/><stop offset="1" stop-color="#00b89c"/>
    </linearGradient>
    <path id="arc-a" d="M105,345 Q273,372 441,322"/>
  </defs>

  <!-- House banner, light -->
  <g class="banner banner--light" transform="translate(73,77)">
    <polygon points="0,100 273,0 546,100 546,463 0,463" fill="var(--teal-deep)"/>
    <polygon points="0,116 273,20 546,116 546,463 0,463" fill="var(--white)"/>
    <text class="brand-name" x="273" y="165" text-anchor="middle" font-size="40">RIDGEVIEW</text>
    <text class="brand-name" x="273" y="200" text-anchor="middle" font-size="22">HOME EXTERIORS</text>
    <text class="web" x="273" y="260" text-anchor="middle" font-size="20">RidgeviewExteriors.Com</text>
    <text class="phone" x="273" y="284" text-anchor="middle" font-size="28">(614) 372 - 9058</text>
    <path d="M0,270 Q273,345 546,270 L546,325 Q273,375 0,335 Z" fill="var(--teal-deep)"/>
    <path d="M0,335 Q273,375 546,325 L546,463 L0,463 Z" fill="var(--gray)"/>
    <text class="slogan" font-size="29"><textPath href="#arc-a" startOffset="50%" text-anchor="middle">Change Begins At Home!</textPath></text>
    <text class="services" x="273" y="396" text-anchor="middle" font-size="19">● ROOFING ● GUTTERS ● EXTERIOR DESIGN ●</text>
    <text class="services" x="288" y="428" text-anchor="middle" font-size="19">● PAINTING ● PRESSURE WASHING ●</text>
    <rect x="12" y="412" width="22" height="42" rx="2" fill="var(--badge-blue)"/>
    <rect x="44" y="438" width="50" height="13" fill="var(--badge-red)"/>
  </g>

  <!-- House banner, charcoal -->
  <g class="banner banner--charcoal" transform="translate(642,77)">
    <polygon points="0,100 273,0 546,100 546,463 0,463" fill="var(--teal-deep)"/>
    <polygon points="0,116 273,20 546,116 546,463 0,463" fill="url(#dark-fade)"/>
    <text class="brand-name" x="273" y="165" text-anchor="middle" font-size="40">RIDGEVIEW</text>
    <text class="brand-name" x="273" y="200" text-anchor="middle" font-size="22">HOME EXTERIORS</text>
    <text class="web web--light" x="273" y="256" text-anchor="middle" font-size="20">RidgeviewExteriors.Com</text>
    <text class="phone" x="273" y="280" text-anchor="middle" font-size="28">(614) 372 - 9058</text>
    <path d="M0,285 Q273,340 546,275 L546,463 L0,463 Z" fill="url(#teal-fade)"/>
    <path d="M0,285 Q273,340 546,275 L546,320 Q273,372 0,330 Z" fill="var(--teal-deep)"/>
    <text class="slogan" font-size="29"><textPath href="#arc-a" startOffset="50%" text-anchor="middle">Change Begins At Home!</textPath></text>
    <text class="services" x="273" y="396" text-anchor="middle" font-size="19">● ROOFING ● GUTTERS ● EXTERIOR DESIGN ●</text>
    <text class="services" x="288" y="428" text-anchor="middle" font-size="19">● PAINTING ● PRESSURE WASHING ●</text>
    <rect x="12" y="412" width="22" height="42" rx="2" fill="var(--badge-blue)"/>
    <rect x="44" y="438" width="50" height="13" fill="var(--badge-red)"/>
  </g>

  <!-- Billboard, black -->
  <g class="billboard billboard--night" transform="translate(258,569)">
    <rect width="793" height="409" fill="url(#night-fade)"/>
    <text class="brand-name" x="148" y="185" text-anchor="middle" font-size="46">RIDGEVIEW</text>
    <text class="brand-name" x="148" y="220" text-anchor="middle" font-size="24">HOME EXTERIORS</text>
    <text class="services" x="522" y="47" text-anchor="middle" font-size="20">● ROOFING ● GUTTERS ● EXTERIOR DESIGN ●</text>
    <text class="services" x="535" y="79" text-anchor="middle" font-size="20">● PAINTING ● PRESSURE WASHING ●</text>
    <text class="web web--light" x="505" y="209" text-anchor="middle" font-size="30">RidgeviewExteriors.Com</text>
    <text class="phone" x="505" y="245" text-anchor="middle" font-size="42">(614) 372 - 9058</text>
    <path d="M0,409 C150,340 290,314 400,314 C540,314 680,345 793,385 L793,409 Z" fill="url(#teal-fade)"/>
    <text class="slogan" x="398" y="374" text-anchor="middle" font-size="34">Change Begins At Home!</text>
    <rect x="12" y="338" width="26" height="42" rx="2" fill="var(--badge-blue)"/>
    <rect x="728" y="361" width="52" height="13" fill="var(--badge-red)"/>
  </g>

  <!-- Billboard, slate -->
  <g class="billboard billboard--slate" transform="translate(258,1006)">
    <rect width="793" height="410" fill="url(#slate-fade)"/>
    <text class="brand-name" x="148" y="185" text-anchor="middle" font-size="46">RIDGEVIEW</text>
    <text class="brand-name" x="148" y="220" text-anchor="middle" font-size="24">HOME EXTERIORS</text>
    <text class="services" x="522" y="47" text-anchor="middle" font-size="20">● ROOFING ● GUTTERS ● EXTERIOR DESIGN ●</text>
    <text class="services" x="535" y="79" text-anchor="middle" font-size="20">● PAINTING ● PRESSURE WASHING ●</text>
    <text class="web web--light" x="505" y="209" text-anchor="middle" font-size="30">RidgeviewExteriors.Com</text>
    <text class="phone" x="505" y="245" text-anchor="middle" font-size="42">(614) 372 - 9058</text>
    <path d="M0,410 C150,340 290,314 400,314 C540,314 680,345 793,385 L793,410 Z" fill="url(#teal-fade)"/>
    <text class="slogan" x="398" y="379" text-anchor="middle" font-size="34">Change Begins At Home!</text>
    <rect x="12" y="338" width="26" height="42" rx="2" fill="var(--badge-blue)"/>
    <rect x="728" y="359" width="52" height="13" fill="var(--badge-red)"/>
  </g>
</svg>
</body>
</html>
```